Business Card Design needed for logo design project

Our business needs a business card design. I'm not sure what format files are generally delivered back, but clearly I will need the ability to edit to add colleagues contact details.

Our logo is attached.

Brivanor is a 3D design services company, providing app, serious/educational game, VR and AR websites/applications to corporate clients.

Target Market(s)

Corporate blue-chip clients needing 3D design services

Industry/Entity Type

Business

Font styles to use
Sans Serif

Requirements
Must have
• Templated such that I can add details (name, phone number etc). Needs to include logo from previous project winner - attached.

```html
<!DOCTYPE html>
<html lang="en">
<head>
<meta charset="utf-8">
<title>Brivanor Business Card</title>
<link href="https://fonts.googleapis.com/css2?family=Lato:wght@300;400;700;900&display=swap" rel="stylesheet">
<style>
  :root {
    --red: #f2112a;
    --red-light: #f6505f;
    --red-deep: #ff0010;
    --ink: #3a3a3c;
    --muted: #555558;
    --paper: #f7f7f7;
    --backdrop: #e4e4e6;
  }
  * { margin: 0; padding: 0; box-sizing: border-box; }
  html, body { width: 1200px; height: 905px; overflow: hidden; }
  body {
    background: var(--backdrop);
    font-family: "Lato", sans-serif;
    display: flex;
    flex-direction: column;
    align-items: center;
    justify-content: center;
    gap: 48px;
  }
  .card {
    width: 660px;
    height: 377px;
    position: relative;
    overflow: hidden;
    box-shadow: 0 6px 18px rgba(0,0,0,0.18);
  }
  /* Back side */
  .card-back {
    background: linear-gradient(110deg, var(--red-light) 0%, var(--red) 55%, var(--red-deep) 100%);
  }
  .card-back .brand {
    position: absolute;
    right: 58px;
    bottom: 92px;
    display: flex;
    align-items: center;
    gap: 18px;
  }
  .card-back .brand-dot {
    width: 68px; height: 68px;
    border-radius: 50%;
    background: #ffffff;
  }
  .card-back .brand-name {
    color: #ffffff;
    font-weight: 300;
    font-size: 62px;
    letter-spacing: 1px;
    line-height: 1;
  }
  /* Front side */
  .card-front { background: var(--paper); }
  .card-front .side-band {
    position: absolute; left: 0; top: 0; bottom: 0;
    width: 40px;
    background: linear-gradient(180deg, var(--red-light), var(--red));
  }
  .holder {
    position: absolute; left: 72px; top: 48px;
  }
  .holder-name {
    color: var(--red);
    font-weight: 900;
    font-size: 27px;
    letter-spacing: 0.5px;
    line-height: 1;
  }
  .holder-role {
    color: var(--muted);
    font-size: 14px;
    letter-spacing: 0.5px;
    margin-top: 2px;
  }
  .address {
    position: absolute; left: 72px; top: 158px;
    color: var(--ink);
    font-size: 15px;
    line-height: 1.25;
    letter-spacing: 0.4px;
  }
  .contacts {
    position: absolute; left: 72px; top: 220px;
    list-style: none;
    color: var(--ink);
    font-size: 15px;
    letter-spacing: 0.4px;
  }
  .contacts li {
    display: flex; align-items: center; gap: 10px;
    height: 23px;
  }
  .contacts svg { width: 15px; height: 15px; fill: var(--red); flex: none; }
  .card-front .brand {
    position: absolute;
    right: 48px; top: 170px;
    display: flex; align-items: center; gap: 14px;
  }
  .card-front .brand-dot {
    width: 50px; height: 50px;
    border-radius: 50%;
    background: var(--red);
  }
  .card-front .brand-name {
    color: var(--ink);
    font-weight: 300;
    font-size: 46px;
    letter-spacing: 1px;
    line-height: 1;
  }
</style>
</head>
<body>
  <section class="card card-back" aria-label="Card back">
    <div class="brand">
      <span class="brand-dot"></span>
      <span class="brand-name">BRIVANOR</span>
    </div>
  </section>

  <section class="card card-front" aria-label="Card front">
    <div class="side-band"></div>
    <div class="holder">
      <p class="holder-name">YOUR NAME</p>
      <p class="holder-role">DIRECTOR</p>
    </div>
    <p class="address">UNIT 31, HARBOUR LANE<br>NORTHFIELD CITY</p>
    <ul class="contacts">
      <li>
        <svg viewBox="0 0 16 16" aria-hidden="true"><path d="M2 5c0-2 2-3 6-3s6 1 6 3v1h-3V5H5v1H2zM4 7h8l2 7H2z"/></svg>
        9850142765310
      </li>
      <li>
        <svg viewBox="0 0 16 16" aria-hidden="true"><path d="M4 1h8v14H4zM5.5 3v9h5V3zM7 13h2v1H7z" fill-rule="evenodd"/></svg>
        8801700456218
      </li>
      <li>
        <svg viewBox="0 0 16 16" aria-hidden="true"><path d="M1 3h14v10H1zM2.5 4.5 8 9l5.5-4.5v7h-11z" fill-rule="evenodd"/></svg>
        YOURMAIL@BRIVANOR.COM
      </li>
      <li>
        <svg viewBox="0 0 16 16" aria-hidden="true"><path d="M1 2h14v9H1zM2.5 3.5v6h11v-6zM7 11h2v2h3v1H4v-1h3z" fill-rule="evenodd"/></svg>
        WWW.BRIVANOR.COM
      </li>
    </ul>
    <div class="brand">
      <span class="brand-dot"></span>
      <span class="brand-name">BRIVANOR</span>
    </div>
  </section>
</body>
</html>
```